Test and Tag business card design

We are an appliance test and tag company in Brisbane Australia requiring a business card design.
I don't have a logo.
Card front: Matte black background with white font.
Card back: White background with black font colour
Examples are attached
Minimalist design
Reason: Looking for more designs with an extreme minimal feel
Industry/Entity Type
Appliance
Contact Information for Business Card
Business name: Summit Check and Label
Description: Onsite Electrical Testing and Tagging
Licence No. 48213
Name: Greg Palmby
Mobile: 0417 592 348
Email: greg@summitcheckandlabel.com.au
Web: summitcheckandlabel.com.au
Logo Text
Summit Check and Label
Look and feel

```html
<!DOCTYPE html>
<html lang="en">
<head>
<meta charset="utf-8">
<title>Summit Check and Label – Business Card</title>
<link rel="stylesheet" href="https://fonts.googleapis.com/css2?family=Josefin+Sans:wght@300;400&display=swap">
<style>
  :root {
    --backdrop: #d6d4d2;
    --card-white: #ffffff;
    --card-black: #0d0d0d;
    --ink-dark: #1a1a1a;
    --ink-light: #f2f2f2;
    --ink-muted: #bdbdbd;
    --divider: rgba(255,255,255,0.55);
  }
  * { margin: 0; padding: 0; box-sizing: border-box; }
  html, body {
    width: 1200px; height: 1000px; overflow: hidden;
    background: var(--backdrop);
    font-family: "Josefin Sans", "Futura", sans-serif;
    font-weight: 300;
  }
  .canvas {
    position: relative; width: 1200px; height: 1000px;
    display: flex; flex-direction: column; align-items: center; justify-content: center;
    gap: 32px;
  }
  .card {
    position: relative; width: 800px; height: 457px;
    box-shadow: 0 4px 18px rgba(0,0,0,0.18);
  }
  .card--back { background: var(--card-white); }
  .card--front { background: var(--card-black); color: var(--ink-light); }

  .wordmark {
    position: absolute; white-space: nowrap;
    font-weight: 300; letter-spacing: -0.5px;
  }
  .card--back .wordmark {
    left: 50%; top: 50%; transform: translate(-50%, -50%);
    font-size: 36px; color: var(--ink-dark);
  }
  .card--front .wordmark {
    left: 40px; top: 46%; transform: translateY(-50%);
    font-size: 27px; color: var(--ink-light);
  }

  .divider {
    position: absolute; left: 42%; top: 24%; width: 1px; height: 48%;
    background: linear-gradient(to bottom, transparent, var(--divider) 30%, var(--divider) 70%, transparent);
  }

  .contact { position: absolute; left: 50.6%; top: 31%; }
  .contact__name { font-size: 30px; font-weight: 400; letter-spacing: 0.5px; margin-bottom: 22px; }
  .contact__list { list-style: none; font-size: 19px; line-height: 30px; color: var(--ink-muted); }
  .contact__label { margin-right: 6px; }

  .tagline {
    position: absolute; left: 0; right: 0; bottom: 22px; text-align: center;
    font-size: 15px; font-weight: 400; letter-spacing: 0.4px; color: var(--ink-light);
  }
</style>
</head>
<body>
<main class="canvas">
  <section class="card card--back" aria-label="Card back">
    <div class="wordmark">summit check &amp; label</div>
  </section>

  <section class="card card--front" aria-label="Card front">
    <div class="wordmark">summit check &amp; label</div>
    <div class="divider"></div>
    <div class="contact">
      <p class="contact__name">Greg Palmby</p>
      <ul class="contact__list">
        <li><span class="contact__label">m.</span>0417 592 348</li>
        <li><span class="contact__label">e.</span>greg@summitcheckandlabel.com.au</li>
        <li><span class="contact__label">w.</span>www.summitcheckandlabel.com.au</li>
      </ul>
    </div>
    <p class="tagline">Onsite Electrical Testing &amp; Tagging – Licence No. 48213</p>
  </section>
</main>
</body>
</html>
```